Bluestone Nine LLC Flyer Design

Marketing Materials for Real Estate Company. This flyer will be used to promote the company throughout the Commercial Real Estate business in the United States. The team has been together for 15 years. We are the middle guys between the Tenant, Broker, and the Owner. In the case of working with a Franchisor, we will be their Plug and Play leasing arm that will assist their new Franchisee's with their site selection, lease negotiations, design and construction management.

Target Market(s)

Real Estate Owners, Franchisor's, and Brokers

Font styles to use
Serif

Colors

Designer to choose colors to be used in the design.

Requirements
Must have
• The flyer must have......
• 1. The Best Leasing Machine On The Planet
• 2. Over the past 15 years our group has completed 4,492 lease transactions resulting in leasing 17,803,114 square feet in shopping centers across the United States.
• 3. Plug and Play Leasing Specialists. We handle the details between when the broker shows up with the space and the tenant and completing the lease negotiations, legal negotiations and documentation, and construction management to Certificate of Occupancy.
• 4. For Information Call Colette Varga at 555-014-2763 or Wendy Falk at 555-017-8302.
Nice to have
• National Tenants the we have completed transactions with....
• Pellmart, Fresh Basket, Harbor Pams, Vexo, Dunn, QV Rendo, Burrasco, Pattersons, Wrap Shack, Brewhorns, Summit Workout, ShipVo, Tredwell, PKN, Halvorsons, Q&L, Ledger Union Bank, Hen Haus-O, Lotus Kitchen, Furvo, Dex-Mart, Fieldly, and Orbit Theaters

```html
<!DOCTYPE html>
<html lang="en">
<head>
<meta charset="utf-8">
<title>Bluestone Nine LLC Flyer</title>
<link rel="stylesheet" href="https://fonts.googleapis.com/css2?family=Open+Sans:wght@400;600&family=Tinos:ital,wght@0,400;0,700;1,400&display=swap">
<style>
  :root {
    --band-green: #78d180;
    --brand-green: #8cc157;
    --deep-green: #1f7a30;
    --mid-green: #3f9f4a;
    --ink: #111111;
    --paper: #ffffff;
  }
  * { margin: 0; padding: 0; box-sizing: border-box; }
  html, body { width: 777px; height: 1200px; overflow: hidden; background: var(--paper); }
  .flyer { position: relative; width: 777px; height: 1200px; overflow: hidden; background: var(--paper); font-family: "Tinos", "Times New Roman", serif; color: var(--ink); }
  .backdrop { position: absolute; inset: 0; }
  .brand-name { position: absolute; left: 2px; top: 178px; font-family: "Open Sans", Arial, sans-serif; font-weight: 600; font-size: 55px; letter-spacing: 3px; color: var(--brand-green); white-space: nowrap; }
  .tagline { position: absolute; left: 177px; top: 264px; font-weight: 700; font-size: 25px; letter-spacing: 1.3px; white-space: nowrap; }
  .track-record { position: absolute; left: 27px; top: 319px; font-size: 23px; line-height: 27.5px; white-space: nowrap; }
  .specialists-title { position: absolute; left: 294px; top: 580px; font-size: 27px; color: var(--paper); letter-spacing: 0.6px; white-space: nowrap; }
  .specialists-body { position: absolute; left: 294px; top: 628px; font-size: 20.5px; line-height: 21.6px; white-space: nowrap; letter-spacing: 0.2px; }
  .tenants-title { position: absolute; left: 11px; top: 832px; font-weight: 700; font-size: 19px; line-height: 21px; color: var(--paper); letter-spacing: 0.5px; white-space: nowrap; }
  .tenants-list { position: absolute; left: 11px; top: 884px; font-size: 15.6px; line-height: 21.6px; white-space: nowrap; }
  .info-call { position: absolute; left: 508px; top: 850px; font-family: "Open Sans", Arial, sans-serif; font-size: 24px; letter-spacing: 0.8px; white-space: nowrap; }
  .contact { position: absolute; font-size: 27px; letter-spacing: -1.2px; white-space: nowrap; }
  .contact .name { color: var(--paper); }
  .contact .at { color: var(--paper); font-style: italic; font-size: 22px; }
  .contact .phone { color: var(--ink); font-weight: 700; }
  .contact-first { left: 357px; top: 924px; }
  .contact-second { left: 398px; top: 976px; }
</style>
</head>
<body>
<main class="flyer">
  <svg class="backdrop" width="777" height="1200" viewBox="0 0 777 1200" aria-hidden="false">
    <defs>
      <linearGradient id="cityTone" x1="0" y1="0" x2="0" y2="1">
        <stop offset="0" stop-color="#b99a78"/>
        <stop offset="0.45" stop-color="#6f5a48"/>
        <stop offset="1" stop-color="#2e2723"/>
      </linearGradient>
      <linearGradient id="parkTone" x1="0" y1="0" x2="0" y2="1">
        <stop offset="0" stop-color="#a9d4ee"/>
        <stop offset="0.4" stop-color="#c7c1ae"/>
        <stop offset="0.7" stop-color="#4f8a3f"/>
        <stop offset="1" stop-color="#c9bda7"/>
      </linearGradient>
      <linearGradient id="officeTone" x1="0" y1="0" x2="1" y2="1">
        <stop offset="0" stop-color="#8d5a3a"/>
        <stop offset="0.5" stop-color="#c9c5bd"/>
        <stop offset="1" stop-color="#7a4c30"/>
      </linearGradient>
      <linearGradient id="skylineTone" x1="0" y1="0" x2="0" y2="1">
        <stop offset="0" stop-color="#78d180"/>
        <stop offset="0.35" stop-color="#4fae57"/>
        <stop offset="1" stop-color="#1f7a30"/>
      </linearGradient>
    </defs>

    <path class="city-photo" role="img" aria-label="Aerial photograph of a downtown skyline at dusk" fill="url(#cityTone)"
      d="M0,0 H777 V257 C730,215 680,185 560,165 C420,150 330,170 250,160 C150,148 60,120 0,88 Z"/>

    <path class="band band-top" fill="var(--band-green)"
      d="M0,292 C150,262 330,262 430,278 C560,296 680,300 777,300 V525 C600,505 400,488 250,488 C150,486 60,480 0,485 Z"/>
    <circle class="park-photo" role="img" aria-label="Aerial photograph of a city park surrounded by buildings" cx="652" cy="425" r="125" fill="url(#parkTone)"/>

    <path class="band band-middle" fill="var(--band-green)"
      d="M0,505 C200,515 450,560 777,540 V760 C600,770 400,788 250,792 C150,794 60,790 0,796 Z"/>
    <circle class="office-photo" role="img" aria-label="Photograph of an open office with cubicles seen from above" cx="136" cy="650" r="143" fill="url(#officeTone)"/>

    <path class="band band-bottom" fill="var(--band-green)"
      d="M0,812 C200,800 400,790 777,770 V1200 H0 Z"/>

    <circle class="contact-bubble" cx="478" cy="858" r="47" fill="var(--paper)"/>
    <path class="contact-bubble" fill="var(--paper)"
      d="M525,800 C540,778 600,776 620,795 C660,786 710,790 777,800 V1030 C740,1050 680,1040 640,1005 C600,975 560,940 525,900 Z"/>

    <g class="phone-icon" fill="var(--brand-green)">
      <path d="M466,842 l7,-4 l7,11 l-6,4 c2,7 6,13 12,17 l5,-5 l10,8 l-4,7 c-4,3 -10,3 -15,0 c-11,-7 -19,-19 -21,-31 c0,-3 2,-6 5,-7 Z"/>
    </g>

    <rect class="skyline" role="img" aria-label="Green illustrated city skyline silhouette" x="0" y="1030" width="777" height="140" fill="url(#skylineTone)"/>
    <path class="base-band" fill="var(--deep-green)" d="M0,1172 C250,1160 520,1182 777,1168 V1200 H0 Z"/>
    <path class="base-line" fill="none" stroke="var(--paper)" stroke-width="3" d="M0,1170 C250,1158 520,1180 777,1166"/>
  </svg>

  <h1 class="brand-name">Bluestone Nine LLC</h1>
  <p class="tagline">The Best Leasing Machine On The Planet</p>

  <p class="track-record">&nbsp;Over the past 15 years our group has completed<br>4,492 lease transactions resulting in leasing<br>17,803,114 square feet in shopping centers<br>across the United States.</p>

  <h2 class="specialists-title">Plug and Play Leasing Specialists</h2>
  <p class="specialists-body">We handle the details between when the<br>broker shows up with the space and the tenant<br>and completing the lease negotiations, legal<br>negotiations and documentation, and construc-<br>tion management to Certificate of Occupancy.</p>

  <h3 class="tenants-title">National Tenants the we have<br>completed transactions with....</h3>
  <p class="tenants-list">Pellmart, Fresh Basket, Harbor Pams, Vexo, Dunn,<br>QV Rendo, Burrasco, Pattersons, Wrap Shack,<br>Brewhorns, Summit Workout, ShipVo, Tredwell,<br>PKN, Halvorsons, Q&amp;L, Ledger Union Bank,<br>Hen Haus-O, Lotus Kitchen, Furvo, Dex-Mart,<br>Fieldly, and Orbit Theaters</p>

  <p class="info-call">For Information Call</p>
  <p class="contact contact-first"><span class="name">Colette Varga</span> <span class="at">at</span><span class="phone">555-014-2763</span></p>
  <p class="contact contact-second"><span class="name">Wendy Falk</span> <span class="at">at</span><span class="phone">555-017-8302</span></p>
</main>
</body>
</html>
```